Dating Coach needs a Book Cover Design

My new book called "Where the Lanterns Gather: Meeting Someone Worth Knowing in a Crowded Digital Age" needs a cover! I tried to make one on my own, but it's just not my skill set :) Please see attached for my best attempt. I'd like to see the title smaller and the tagline bigger - so that the tagline is easier to read. But I'm not sure how to do this and still have the Title look great. I'm also considering if the "WHERE LANTERNS GATHER" part should not be in all caps. Looking forward to your ideas! I'm also afraid that the drawing is a bit too cartoonish and doesn't match my brand. I'm looking for something elegant and also very approachable and down to earth. My website is www.gretavondlecounsel.example so you can use as reference! Please see my attached brand style guide for colors. This will be an e-book that I give away for free to anyone who signs up for my newsletter. Some mock-ups would also be great to use in advertising.

```html
<!DOCTYPE html>
<html lang="en">
<head>
<meta charset="utf-8">
<title>Where the Lanterns Gather — Book Cover</title>
<link rel="stylesheet" href="https://fonts.googleapis.com/css2?family=Gilda+Display&display=swap">
<style>
  :root {
    --backdrop: #766779;
    --cover: #a083a8;
    --cream: #f1e2d2;
    --text-glow: rgba(90, 60, 95, 0.45);
    --straw-light: #f0c35a;
    --straw-mid: #d9a03a;
    --straw-deep: #b57e22;
    --ground-shadow: rgba(110, 70, 120, 0.55);
  }
  * { margin: 0; padding: 0; box-sizing: border-box; }
  html, body {
    width: 1200px;
    height: 1001px;
    overflow: hidden;
    background: var(--backdrop);
  }
  .book-cover {
    position: absolute;
    left: 247px;
    top: 20px;
    width: 706px;
    height: 960px;
    background: var(--cover);
    color: var(--cream);
    font-family: "Gilda Display", "Times New Roman", serif;
    text-align: center;
  }
  .title-block {
    position: absolute;
    left: 0;
    right: 0;
    top: 52px;
    line-height: 0.9;
    text-shadow: 0 4px 14px var(--text-glow);
    font-weight: 400;
  }
  .title-lead {
    display: block;
    font-size: 56px;
    letter-spacing: -0.5px;
  }
  .title-main {
    display: block;
    font-size: 104px;
    letter-spacing: -3px;
  }
  .title-main.last {
    font-size: 112px;
  }
  .tagline {
    position: absolute;
    left: 0;
    right: 0;
    top: 340px;
    font-size: 33px;
    line-height: 1.2;
    letter-spacing: -0.3px;
    text-shadow: 0 3px 10px var(--text-glow);
  }
  .cover-art {
    position: absolute;
    left: 98px;
    top: 456px;
    width: 470px;
    height: 367px;
    border-radius: 46% 46% 40% 40% / 42% 42% 50% 50%;
    background:
      radial-gradient(ellipse 60% 60% at 55% 42%, var(--straw-light), var(--straw-mid) 60%, rgba(181,126,34,0) 100%),
      radial-gradient(ellipse 50% 12% at 55% 92%, var(--ground-shadow), rgba(110,70,120,0) 100%);
  }
  .author {
    position: absolute;
    left: 0;
    right: 0;
    top: 838px;
    font-size: 43px;
    letter-spacing: -0.5px;
    text-shadow: 0 3px 10px var(--text-glow);
  }
</style>
</head>
<body>
  <main class="book-cover">
    <h1 class="title-block">
      <span class="title-lead">Where the</span>
      <span class="title-main">Lanterns</span>
      <span class="title-main last">Gather</span>
    </h1>
    <p class="tagline">Meeting someone worth knowing<br>in a crowded digital age</p>
    <div class="cover-art" role="img" aria-label="Golden straw heart sitting on scattered straw, with a small white outlined heart drawn at its left side"></div>
    <p class="author">Greta Vondle</p>
  </main>
</body>
</html>
```